TARPLOAD business card design

TARPLOAD is a manufacturer of skip bags supplying both the domestic and commercial market. We wish to convey core characteristics of strength, professionalism and reliability to our customers. We are after a business card that uses our company colours of black and yellow as well as incorporating our logo. Our customers are predominantly in the construction or hardware industry. It is important the cards are professional as we are a small company wishing to appear larger than we actually are. more info on the company and product available at www.tarpload-example.com.au

Target Market(s)

hardware buyers, contruction company owners

Industry/Entity Type

Construction

Requirements
Must have
• company colours of black and yellow - No other colours or variation of yellow black. our company logo. card design must convey "tough"
• Card design must be landscape
• Details to be included on the card are:
• Name and Tiltle
• Phone number : 1300 41 62 53
• Mobile: 0452 718 903
• Fax: 03 9617 4852
• email: dale.hendry@tarpload-example.com.au
• address: PO Box 517, Kelvindale, VIC,3294
• Text in white when on a black background
Nice to have
• I like the idea of the back of the card being black with lighter circle area in the middle with black logo in the centre. Similar to the attached "iconic" card

```html
<!DOCTYPE html>
<html lang="en">
<head>
<meta charset="utf-8">
<title>TARPLOAD business card</title>
<link href="https://fonts.googleapis.com/css2?family=Arimo:wght@400;700&family=Open+Sans:wght@400&display=swap" rel="stylesheet">
<style>
  :root {
    --yellow: #d4b017;
    --black: #1c1a1a;
    --white: #ffffff;
    --grey-light: #a3a3a3;
    --grey-dark: #1f1f1f;
    --ink: #1c1a1a;
  }
  html, body {
    margin: 0;
    padding: 0;
    width: 1200px;
    height: 343px;
    overflow: hidden;
    background: var(--white);
  }
  .card-sheet {
    position: relative;
    width: 1200px;
    height: 343px;
    background: var(--white);
  }
  .side { position: absolute; top: 0; height: 343px; }
  .front { left: 0; width: 598px; }
  .back { left: 598px; width: 602px; }

  .stripe { position: absolute; left: 0; right: 0; }
  .front .stripe { background: var(--yellow); }
  .back .stripe { background: var(--black); }
  .stripe.top { top: 0; height: 14px; }
  .stripe.bottom { top: 328px; height: 13px; }

  .front .panel-upper {
    position: absolute; left: 0; right: 0; top: 20px; height: 118px;
    background: var(--yellow);
  }
  .front .title-band {
    position: absolute; left: 0; right: 0; top: 138px; height: 57px;
    background: var(--white);
  }
  .front .panel-lower {
    position: absolute; left: 0; right: 0; top: 195px; height: 127px;
    background: var(--yellow);
  }

  .brand-mark {
    position: absolute; left: 26px; top: 60px;
    display: flex; align-items: center; gap: 6px;
    font-family: "Arimo", Arial, sans-serif;
    font-weight: 700;
    font-size: 19px;
    color: var(--ink);
    letter-spacing: 0.5px;
  }
  .brand-mark .brand-square {
    width: 12px; height: 12px; background: var(--ink);
  }

  .person-name {
    position: absolute; left: 194px; top: 44px;
    margin: 0;
    font-family: "Arimo", Arial, sans-serif;
    font-weight: 400;
    font-size: 57px;
    line-height: 1;
    color: var(--ink);
  }
  .person-title {
    position: absolute; left: 220px; top: 8px;
    margin: 0;
    font-family: "Open Sans", Arial, sans-serif;
    font-size: 33px;
    line-height: 1.1;
    color: var(--ink);
  }

  .contact-list {
    position: absolute; top: 218px;
    margin: 0; padding: 0; list-style: none;
    font-family: "Open Sans", Arial, sans-serif;
    font-size: 18px;
    color: var(--ink);
  }
  .contact-list.phones { left: 47px; }
  .contact-list.mail { left: 232px; }
  .contact-list li {
    display: flex; align-items: center;
    height: 30px;
  }
  .contact-list .icon {
    width: 20px; height: 20px; margin-right: 7px; flex: none;
  }
  .contact-list.mail .icon { margin-right: 9px; }

  .back .spotlight {
    position: absolute; left: 0; right: 0; top: 20px; height: 302px;
    background: radial-gradient(ellipse 55% 75% at 50% 50%, var(--grey-light) 0%, #6a6868 45%, var(--grey-dark) 100%);
  }
  .back-brand {
    position: absolute; left: 0; right: 0; top: 0; bottom: 0;
    display: flex; align-items: center; justify-content: center; gap: 14px;
    font-family: "Arimo", Arial, sans-serif;
    font-weight: 700;
    font-size: 46px;
    color: var(--ink);
    letter-spacing: 1px;
  }
  .back-brand .brand-square {
    width: 30px; height: 30px; background: var(--ink);
  }
</style>
</head>
<body>
<main class="card-sheet">
  <section class="side front" aria-label="Card front">
    <div class="stripe top"></div>
    <div class="panel-upper">
      <div class="brand-mark"><span class="brand-square"></span>TARPLOAD</div>
      <h1 class="person-name">Brock Mallard</h1>
    </div>
    <div class="title-band">
      <p class="person-title">manager</p>
    </div>
    <div class="panel-lower"></div>

    <ul class="contact-list phones">
      <li>
        <svg class="icon" viewBox="0 0 20 20" aria-hidden="true">
          <path d="M2 8 Q10 2 18 8 L16 10 L13 8 L13 6 Q10 5 7 6 L7 8 L4 10 Z" fill="#fff"/>
          <path d="M5 11 L15 11 L17 17 L3 17 Z" fill="#fff"/>
          <circle cx="10" cy="14" r="2" fill="var(--yellow)"/>
        </svg>1300 41 62 53
      </li>
      <li>
        <svg class="icon" viewBox="0 0 20 20" aria-hidden="true">
          <rect x="6" y="1" width="9" height="18" rx="1.5" fill="none" stroke="#fff" stroke-width="1.6"/>
          <rect x="8" y="3.5" width="5" height="5" fill="#fff"/>
          <g fill="#fff"><rect x="8" y="10" width="1.4" height="1.4"/><rect x="10" y="10" width="1.4" height="1.4"/><rect x="12" y="10" width="1.4" height="1.4"/><rect x="8" y="12.5" width="1.4" height="1.4"/><rect x="10" y="12.5" width="1.4" height="1.4"/><rect x="12" y="12.5" width="1.4" height="1.4"/><rect x="8" y="15" width="1.4" height="1.4"/><rect x="10" y="15" width="1.4" height="1.4"/><rect x="12" y="15" width="1.4" height="1.4"/></g>
        </svg>0452 718 903
      </li>
      <li>
        <svg class="icon" viewBox="0 0 20 20" aria-hidden="true">
          <rect x="5" y="1.5" width="10" height="6" fill="none" stroke="#fff" stroke-width="1.6"/>
          <rect x="1.5" y="7.5" width="17" height="7" rx="2" fill="none" stroke="#fff" stroke-width="1.6"/>
          <rect x="5" y="12" width="10" height="6.5" fill="var(--yellow)" stroke="#fff" stroke-width="1.6"/>
        </svg>03 9617 4852
      </li>
    </ul>

    <ul class="contact-list mail">
      <li>
        <svg class="icon" viewBox="0 0 20 20" aria-hidden="true">
          <rect x="1" y="4" width="18" height="12" fill="none" stroke="#fff" stroke-width="1.6"/>
          <path d="M1 4 L10 11 L19 4" fill="none" stroke="#fff" stroke-width="1.6"/>
        </svg>PO Box 517, Kelvindale, VIC,3294
      </li>
      <li>
        <svg class="icon" viewBox="0 0 20 20" aria-hidden="true">
          <rect x="1" y="3" width="18" height="14" rx="1.5" fill="none" stroke="#fff" stroke-width="1.6"/>
          <text x="10" y="14.5" text-anchor="middle" font-family="Arial, sans-serif" font-size="12" fill="#fff">@</text>
        </svg>dale.hendry@tarpload-example.com.au
      </li>
    </ul>

    <div class="stripe bottom"></div>
  </section>

  <section class="side back" aria-label="Card back">
    <div class="stripe top"></div>
    <div class="spotlight">
      <div class="back-brand"><span class="brand-square"></span>TARPLOAD</div>
    </div>
    <div class="stripe bottom"></div>
  </section>
</main>
</body>
</html>
```